Header for website Size is 1000px x 120px
I have CS5 so will need the source files photoshop, illustrator etc, so I can change text and photos.
Photos attached, includes example header and screenshot of eg site
Brief:
I need a website header for golfers where I can change the photos and their name.
The header needs to have these things.
- pictures of the golfer (use from pics attached)
- Their name
- Also under there name is smaller text I need a line of text you can just say "Offical Website" in your e.g to me
so for example you should have
Dale Forsythe
Offical Website
And some photos that are blended with some nice golf background or some grass or other ideas that you come up with that will look better than mine I'm sure :)
Size is 1000px x 120px
It needs to look professional and blend in nicely. I don't mind how many photos are used maybe 1-4?
The text needs to look professional too but not boring.
The header you create will be used on a website for a Professional Golfer (tour pro) their job is golf, their website needs to showcase them and promote them as best as possible.
As I said above I will need to swap photos easily and edit the text so will need the source files.
So a important point here. I guess there is no need to blend or do anything to the photos you add as I will actually need to change the photos and just need a simple template that I can swap photos and edit their name.
Ultimately I would like 3 versions of the header done and source files for all 3 so I can give them(the golfers) a choice of header type.
See how you go.
Remember that the header must have the ability for me to easily swap images and of course change the text.
My goal is to use the same header for each golfer but obviously with their images and their name.
I have CS5 so will need the source files photoshop, illustrator etc
2 example headers are attached to show you my attempts :) Please do something better.
I don't want any flash.

```html
<!DOCTYPE html>
<html lang="en">
<head>
<meta charset="utf-8">
<title>Dale Forsythe – Offical Website</title>
<link rel="stylesheet" href="https://fonts.googleapis.com/css2?family=Open+Sans:wght@400;700&family=PT+Sans:wght@400;700&display=swap">
<style>
  :root {
    --backdrop: #3a4147;
    --page: #f3f5f6;
    --panel-line: #dcdfe1;
    --header-dark: #1d211c;
    --banner: rgba(20, 22, 20, 0.78);
    --nav-top: #5a9bff;
    --nav-mid: #2f78fb;
    --nav-bottom: #1a56e6;
    --accent: #2f73e0;
    --text: #333a40;
    --muted: #5d656b;
    --cell: #eceff0;
    --cell-head: #e1e5e6;
    --white: #ffffff;
  }
  * { box-sizing: border-box; margin: 0; padding: 0; }
  html, body {
    width: 1200px; height: 818px; overflow: hidden;
    background: var(--backdrop);
    font-family: "PT Sans", Arial, sans-serif;
    color: var(--text);
  }
  .site {
    position: absolute; left: 44px; top: 37px;
    width: 1108px; height: 781px;
    background: var(--page);
    overflow: hidden;
  }
  /* Header */
  .site-header {
    position: absolute; left: 0; top: 0; width: 1108px; height: 135px;
    background: var(--header-dark);
  }
  .header-photo {
    position: absolute; right: 0; top: 0; width: 620px; height: 135px;
    background: linear-gradient(90deg, #1d211c 0%, #3b4533 30%, #6c6e5c 55%, #8f8c80 75%, #3d4636 100%);
  }
  .portrait {
    position: absolute; left: 7px; top: 6px; width: 181px; height: 120px;
    border: 3px solid var(--white);
    background: linear-gradient(160deg, #5f8a34 0%, #7a9b4a 45%, #b9a58c 75%, #e8e6e0 100%);
  }
  .name-banner {
    position: absolute; left: 188px; top: 26px; width: 540px; height: 79px;
    background: linear-gradient(90deg, var(--banner) 0%, var(--banner) 70%, rgba(20,22,20,0) 100%);
    padding: 6px 0 0 12px;
  }
  .golfer-name {
    font-family: "Open Sans", Arial, sans-serif;
    font-weight: 400; font-size: 44px; line-height: 48px;
    color: var(--white); text-transform: uppercase; letter-spacing: 0.5px;
  }
  .tagline {
    font-family: "Open Sans", Arial, sans-serif;
    font-weight: 700; font-size: 16px; line-height: 20px;
    color: var(--white); text-transform: uppercase; margin-top: 1px;
  }
  /* Navigation */
  .main-nav {
    position: absolute; left: 0; top: 135px; width: 1108px; height: 65px;
    background: linear-gradient(180deg, var(--nav-top) 0%, var(--nav-mid) 40%, var(--nav-mid) 70%, var(--nav-bottom) 100%);
  }
  .main-nav a {
    position: absolute; top: 14px;
    font-size: 16.5px; font-weight: 700; color: var(--white); text-decoration: none;
    text-transform: uppercase; letter-spacing: -0.2px;
  }
  /* Slider */
  .slider {
    position: absolute; left: 22px; top: 223px; width: 743px; height: 335px;
    background: var(--white); border: 1px solid var(--panel-line);
  }
  .slide-image {
    position: absolute; left: 12px; top: 12px; width: 717px; height: 310px;
    background: linear-gradient(180deg, #4d5f36 0%, #6d7d55 35%, #c9cdc6 60%, #e3e6e2 100%);
  }
  .slider-arrow { position: absolute; top: 145px; }
  .slider-arrow.prev { left: -15px; }
  .slider-arrow.next { left: 724px; }
  /* Articles */
  .section-title {
    position: absolute; font-size: 15.5px; font-weight: 400; color: var(--accent);
  }
  .section-rule {
    position: absolute; height: 2px; background: var(--accent);
  }
  .article-card {
    position: absolute; left: 22px; top: 644px; width: 742px; height: 150px;
    background: var(--white); border: 1px solid var(--panel-line);
    padding: 0 12px;
  }
  .article-title { font-size: 22px; font-weight: 400; color: #222; margin-top: 22px; height: 35px; }
  .article-date { border-top: 1px solid var(--panel-line); border-bottom: 1px solid var(--panel-line); font-size: 12px; color: var(--muted); padding: 5px 0; height: 30px; letter-spacing: 0.3px; }
  .article-body { font-size: 12px; color: var(--muted); margin-top: 20px; letter-spacing: 0.3px; }
  /* Sidebar */
  .follow-row { position: absolute; left: 786px; top: 277px; display: flex; align-items: center; gap: 8px; font-size: 12px; color: var(--text); }
  .follow-button {
    display: flex; align-items: center;
    height: 26px; padding: 0 8px;
    border: 1px solid var(--panel-line); background: var(--white);
    font-size: 12px; color: var(--text);
  }
  .scores {
    position: absolute; left: 789px; top: 382px; width: 294px;
    border-collapse: separate; border-spacing: 3px 3px;
    font-size: 11.5px; line-height: 14.5px; color: #444; letter-spacing: 0.3px;
  }
  .scores th {
    background: var(--cell-head); font-weight: 400; text-transform: uppercase;
    color: #7a8186; font-size: 11.5px; height: 21px; letter-spacing: 0.3px;
  }
  .scores td { background: var(--cell); vertical-align: top; padding: 5px 4px; }
  .scores td.pos, .scores td.score { text-align: center; }
</style>
</head>
<body>
<div class="site">
  <header class="site-header">
    <div class="header-photo" role="img" aria-label="Golfer following through on a tee shot"></div>
    <div class="portrait" role="img" aria-label="Portrait of the golfer in a white cap"></div>
    <div class="name-banner">
      <h1 class="golfer-name">Dale Forsythe</h1>
      <p class="tagline">Offical Website</p>
    </div>
  </header>

  <nav class="main-nav">
    <a href="#" style="left:66px">Home</a>
    <a href="#" style="left:160px">About</a>
    <a href="#" style="left:260px">News</a>
    <a href="#" style="left:353px">Results</a>
    <a href="#" style="left:463px">Schedule</a>
    <a href="#" style="left:589px">Gallery</a>
    <a href="#" style="left:703px">Blog</a>
    <a href="#" style="left:792px">Contact</a>
  </nav>

  <section class="slider">
    <div class="slide-image" role="img" aria-label="Golfer driving from the tee watched by spectators"></div>
    <svg class="slider-arrow prev" width="34" height="42" viewBox="0 0 34 42" aria-hidden="true">
      <path d="M0 0H34V34H0Z" fill="#2f78fb"/><path d="M0 34H16L16 42Z" fill="#173f99"/>
      <path d="M20 8L11 17L20 26" fill="none" stroke="#fff" stroke-width="4"/>
    </svg>
    <svg class="slider-arrow next" width="34" height="42" viewBox="0 0 34 42" aria-hidden="true">
      <path d="M0 0H34V34H0Z" fill="#2f78fb"/><path d="M18 34H34L18 42Z" fill="#173f99"/>
      <path d="M14 8L23 17L14 26" fill="none" stroke="#fff" stroke-width="4"/>
    </svg>
  </section>

  <h2 class="section-title" style="left:22px;top:591px">Latest Articles</h2>
  <div class="section-rule" style="left:22px;top:620px;width:742px"></div>

  <article class="article-card">
    <h3 class="article-title">Kestrel Masters</h3>
    <p class="article-date">Jan - 11 - 2013</p>
    <p class="article-body">testing new post</p>
  </article>

  <h2 class="section-title" style="left:786px;top:233px">Clubroom</h2>
  <div class="section-rule" style="left:786px;top:263px;width:299px"></div>
  <div class="follow-row">
    <span class="follow-button">Follow</span>
    <span>10 members follow this.</span>
  </div>

  <h2 class="section-title" style="left:786px;top:335px">Latest Scores</h2>
  <div class="section-rule" style="left:786px;top:365px;width:299px"></div>

  <table class="scores">
    <colgroup><col style="width:114px"><col style="width:42px"><col style="width:62px"><col style="width:64px"></colgroup>
    <thead><tr><th>Tournament</th><th>Pos</th><th>Score</th><th>Money</th></tr></thead>
    <tbody>
      <tr style="height:69px"><td>Coastal PGA Championship Nov 29 - Dec 02, 2012</td><td class="pos">35</td><td class="score">69-75-<br>72-71<br>287<br>(-1)</td><td>$850</td></tr>
      <tr style="height:67px"><td>2012 Harbour Open Nov 22 - Dec 25, 2012</td><td class="pos">56</td><td class="score">79-72-<br>76-70<br>297<br>(+9)</td><td>$914.4</td></tr>
      <tr style="height:67px"><td>Kestrel Masters Nov 15 - Nov 18, 2012</td><td class="pos">CUT</td><td class="score">77-<br>77--<br>154<br>(+10)</td><td></td></tr>
      <tr style="height:83px"><td>Fernvale Bean House Pro-Am Oct 3 - Oct 4, 2012</td><td class="pos">6</td><td class="score">68-67<br>135<br>(-3)</td><td>$669.4</td></tr>
      <tr style="height:67px"><td>Southern Pro-Am Championship Mar 29 - Apr 1, 2012</td><td class="pos">CUT</td><td class="score">76-71<br>147<br>(+3)</td><td></td></tr>
    </tbody>
  </table>
</div>
</body>
</html>
```